Kentucky residential recovery center needs a flyer design

We need a flyer design for a 16 bed male residential/inpatient recovery center based in Richmond, Kentucky. The facility provides short term (average 30 day) treatment to those struggling with substace abuse and addiction. The design should communicate trust, assurance, safety.
Our wesite provides more information https://brovalcare.org/treatment-services/residential-treatment/

Target Market(s)

Men (typically 30-50) struggling with substance addiction

```html
<!DOCTYPE html>
<html lang="en">
<head>
<meta charset="utf-8">
<title>Broval Care – Reclaim Your Life Today</title>
<link rel="stylesheet" href="https://fonts.googleapis.com/css2?family=Anton&family=Allura&family=Montserrat:wght@400;500;600;700;800&display=swap">
<style>
  :root{
    --navy:#0b0f5e;
    --green:#0b9a2c;
    --orange:#f06a35;
    --gold:#f7a21b;
    --white:#ffffff;
    --ink:#111111;
  }
  *{margin:0;padding:0;box-sizing:border-box;}
  html,body{width:1200px;height:1200px;overflow:hidden;background:var(--white);}
  body{position:relative;font-family:"Montserrat",sans-serif;color:var(--navy);}
  .flyer{position:absolute;left:177px;top:0;width:846px;height:1200px;background:var(--white);overflow:hidden;}
  .shapes{position:absolute;inset:0;width:846px;height:1200px;}
  .abs{position:absolute;}

  .brand{left:186px;top:72px;width:180px;display:flex;align-items:center;gap:8px;}
  .brand-dot{width:26px;height:26px;border-radius:50%;background:var(--navy);flex:none;}
  .brand-name{font-weight:800;font-size:19px;letter-spacing:1px;color:var(--navy);white-space:nowrap;}

  .hero-photo{left:519px;top:93px;width:264px;height:262px;border-radius:48% 52% 50% 50%/46% 50% 50% 54%;
    background:linear-gradient(160deg,#7fb0e6 0%,#b9c6d6 40%,#8a7f78 70%,#c98a7a 100%);}

  .headline-reclaim{left:104px;top:178px;font-family:"Anton",sans-serif;font-size:112px;line-height:1;color:var(--navy);transform:scaleX(.93);transform-origin:left top;letter-spacing:-1px;}
  .headline-your{left:106px;top:272px;width:128px;height:52px;background:var(--orange);transform:skewY(-6deg);display:flex;align-items:center;justify-content:center;}
  .headline-your span{font-weight:600;font-size:29px;color:var(--white);}
  .headline-life{left:220px;top:286px;font-family:"Anton",sans-serif;font-size:68px;line-height:1;color:var(--navy);letter-spacing:2px;transform:scaleX(1.5);transform-origin:left top;}
  .headline-today{left:405px;top:252px;font-family:"Allura",cursive;font-size:88px;line-height:1;color:var(--orange);transform:rotate(-10deg);transform-origin:left center;}

  .intro{left:84px;top:360px;width:380px;text-align:center;font-weight:800;font-size:11.2px;line-height:16.5px;color:var(--ink);}

  .photo{position:absolute;}
  .photo-bedroom{left:286px;top:412px;width:464px;height:295px;border-radius:12px;background:linear-gradient(135deg,#2b2b2e 0%,#4b4038 35%,#9b8a78 65%,#6d5442 100%);}
  .photo-dining{left:95px;top:480px;width:246px;height:157px;border:4px solid var(--white);border-radius:14px;background:linear-gradient(160deg,#e9e6e1 0%,#cfcac3 45%,#2a2522 70%,#5a4a3d 100%);}
  .photo-living{left:165px;top:655px;width:255px;height:195px;border:4px solid var(--white);border-radius:14px;background:linear-gradient(160deg,#e2cfa6 0%,#b49a72 40%,#2a2522 70%,#7b5a4a 100%);}

  .room-label{position:absolute;background:var(--green);color:var(--white);font-weight:500;font-size:16px;letter-spacing:.5px;display:flex;align-items:center;justify-content:center;}
  .label-dining{left:163px;top:609px;width:108px;height:29px;}
  .label-bedroom{left:444px;top:681px;width:145px;height:29px;}
  .label-living{left:224px;top:820px;width:137px;height:29px;}

  .features{left:441px;top:733px;list-style:none;}
  .features li{font-weight:500;font-size:20.5px;line-height:28px;color:var(--navy);display:flex;align-items:center;white-space:nowrap;}
  .features li::before,.problems li::before{content:"";width:0;height:0;border-top:4px solid transparent;border-bottom:4px solid transparent;border-left:5px solid #e5312b;margin-right:7px;flex:none;}

  .problems-band{left:398px;top:897px;width:448px;height:47px;background:var(--navy);display:flex;align-items:center;padding-left:20px;}
  .problems-band h2{font-weight:800;font-size:19.5px;color:var(--white);letter-spacing:.3px;white-space:nowrap;}
  .problems-band h2 em{font-style:normal;color:var(--gold);}
  .problems{left:441px;top:960px;list-style:none;}
  .problems li{font-weight:800;font-size:24px;line-height:33px;color:var(--navy);display:flex;align-items:center;white-space:nowrap;}

  .about{left:65px;top:889px;width:310px;color:var(--white);}
  .about h2{font-weight:500;font-size:23.5px;letter-spacing:.5px;margin-bottom:4px;}
  .about p{font-weight:400;font-size:12.8px;line-height:18px;margin-bottom:18px;}
  .locations{left:64px;top:1101px;width:290px;list-style:none;color:var(--white);}
  .locations li{display:flex;gap:6px;font-size:10.4px;line-height:13px;text-align:center;margin-bottom:13px;}
  .locations svg{flex:none;margin-top:1px;}

  .contact{left:472px;top:1116px;color:var(--white);}
  .contact-phone{display:flex;align-items:center;gap:6px;font-weight:800;font-size:31px;line-height:1;}
  .contact-email{display:flex;align-items:center;gap:4px;font-size:12.5px;margin-top:8px;}
</style>
</head>
<body>
<main class="flyer">
  <svg class="shapes" viewBox="0 0 846 1200" aria-hidden="true">
    <path fill="var(--navy)" d="M545 0 L846 0 L846 608 C800 608 775 590 772 540 C768 470 800 420 790 330 C780 250 720 180 640 150 C590 132 530 125 505 100 C482 75 495 22 545 0 Z"/>
    <path fill="none" stroke="var(--white)" stroke-width="3" d="M726 128 C790 160 810 240 780 300"/>
    <path fill="none" stroke="var(--white)" stroke-width="2" d="M740 122 l12 0 M746 116 l0 12"/>
    <path fill="none" stroke="var(--orange)" stroke-width="2" d="M454 182 l14 0 M461 175 l0 14"/>
    <path fill="var(--green)" d="M756 615 C790 630 820 632 846 630 L846 652 C810 652 780 650 754 642 Z"/>
    <path fill="none" stroke="var(--green)" stroke-width="3" d="M469 385 L745 385 C758 385 765 390 768 400"/>
    <path fill="none" stroke="var(--navy)" stroke-width="4" d="M75 565 L75 485 C75 468 86 460 102 460 L147 460"/>
    <path fill="none" stroke="var(--green)" stroke-width="2" d="M214 458 C235 450 260 446 279 444"/>
    <path fill="var(--navy)" d="M0 808 C90 770 200 765 270 790 C375 835 428 945 424 1056 C422 1120 405 1170 385 1200 L0 1200 Z"/>
    <path fill="none" stroke="var(--green)" stroke-width="3" d="M143 789 L143 845 C143 860 152 869 168 869 L238 869"/>
    <path fill="var(--green)" d="M410 1200 C430 1130 520 1077 640 1077 C740 1077 810 1120 846 1146 L846 1200 Z"/>
  </svg>

  <div class="abs brand"><span class="brand-dot"></span><span class="brand-name">BROVAL CARE</span></div>

  <div class="abs hero-photo" role="img" aria-label="Smiling bearded man outdoors holding a completion certificate"></div>

  <h1>
    <span class="abs headline-reclaim">RECLAIM</span>
    <span class="abs headline-your"><span>YOUR</span></span>
    <span class="abs headline-life">LIFE</span>
    <span class="abs headline-today">Today</span>
  </h1>

  <p class="abs intro">IF YOU'RE GRAPPLING WITH A DRUG ABUSE ISSUE,<br>WE'RE HERE TO ASSIST YOU ON YOUR PATH TO RECOVERY</p>

  <div class="photo photo-bedroom" role="img" aria-label="Bedroom with bunk beds, black bedding and two armchairs"></div>
  <div class="photo photo-dining" role="img" aria-label="Dining room with oval table and black leather chairs"></div>
  <div class="photo photo-living" role="img" aria-label="Living room with leather sofas, rug and wall television"></div>

  <span class="room-label label-dining">DINNING</span>
  <span class="room-label label-bedroom">BEDROOM</span>
  <span class="room-label label-living">LIVINGROOM</span>

  <ul class="abs features">
    <li>30-Day Residential Treatment</li>
    <li>24/7 Supportive Staff</li>
    <li>Individual &amp; Group Therapy</li>
    <li>Safe, Confidential &amp; Trustworthy</li>
    <li>Serene Recover</li>
  </ul>

  <div class="abs problems-band"><h2>PROBLEMS WE <em>CAN HELP WITH</em></h2></div>
  <ul class="abs problems">
    <li>Alcoholism | Drug Addiction</li>
    <li>Medication Addiction</li>
    <li>Behavioral Health</li>
  </ul>

  <section class="abs about">
    <h2>ABOUT US</h2>
    <p>Broval Care Madison County Clinic is a drug &amp; alcohol Rehab facility located in Richmond, KY. Our clinic offers Telemedicine/telehealth, Inpatient &amp; Outpatient treatment specializing in treatment of Adults.</p>
    <p>We also support clients referred from the court/judicial system.</p>
  </section>

  <ul class="abs locations">
    <li><svg width="11" height="15" viewBox="0 0 11 15"><path fill="var(--green)" d="M5.5 0A5.5 5.5 0 0 0 0 5.5C0 9.5 5.5 15 5.5 15S11 9.5 11 5.5A5.5 5.5 0 0 0 5.5 0Zm0 8A2.5 2.5 0 1 1 5.5 3a2.5 2.5 0 0 1 0 5Z"/></svg><span>(Central Ky Clinic) 410 &amp; 412 Maple Ridge Lane,<br>Richmond, Kentucky 40475.</span></li>
    <li><svg width="11" height="15" viewBox="0 0 11 15"><path fill="var(--green)" d="M5.5 0A5.5 5.5 0 0 0 0 5.5C0 9.5 5.5 15 5.5 15S11 9.5 11 5.5A5.5 5.5 0 0 0 5.5 0Zm0 8A2.5 2.5 0 1 1 5.5 3a2.5 2.5 0 0 1 0 5Z"/></svg><span>(Northern Ky Clinic) 2280 Riverbend Court,<br>Burlington, Kentucky 41005.</span></li>
  </ul>

  <div class="abs contact">
    <div class="contact-phone">
      <svg width="28" height="24" viewBox="0 0 28 24" aria-hidden="true"><path fill="var(--white)" d="M2 7C2 3 8 1 14 1s12 2 12 6v2h-6V6c-2-1-10-1-12 0v3H2Z"/><path fill="var(--white)" d="M5 12l3-3h12l3 3v11H5Z"/><g fill="var(--green)"><rect x="9" y="13" width="2.5" height="2.5"/><rect x="12.8" y="13" width="2.5" height="2.5"/><rect x="16.6" y="13" width="2.5" height="2.5"/><rect x="9" y="17" width="2.5" height="2.5"/><rect x="12.8" y="17" width="2.5" height="2.5"/><rect x="16.6" y="17" width="2.5" height="2.5"/></g></svg>
      <span>859) 555-0148</span>
    </div>
    <div class="contact-email">
      <svg width="13" height="10" viewBox="0 0 13 10" aria-hidden="true"><rect width="13" height="10" fill="var(--white)"/><path d="M0 0l6.5 5L13 0" fill="none" stroke="var(--green)" stroke-width="1.2"/></svg>
      <span>admissions@brovalcare.org</span>
    </div>
  </div>
</main>
</body>
</html>
```